!st birthday celebration

Im looking for a celebration type of flyer for our first birthday. something colorful and eye catching but with a vintage feel to it. we are a vintage shop with a friendly atmosphere and always have music playing. I have attached a draft copy i have been working on so far. Thanks

Industry/Entity Type

Shop

```html
<!DOCTYPE html>
<html lang="en">
<head>
<meta charset="utf-8">
<title>Happy 1st Birthday 1920 Vintage</title>
<link rel="stylesheet" href="https://fonts.googleapis.com/css2?family=Josefin+Sans:wght@600&family=Rochester&display=swap">
<style>
  :root {
    --paper-light: #f3dca4;
    --paper-mid: #e8c27e;
    --paper-edge: #d9a95c;
    --tone-green: #4f8637;
    --tone-teal: #2f8a80;
    --tone-mustard: #b58d28;
    --tone-orange: #c0591c;
    --tone-red: #9a2b1e;
    --ink: #27231f;
    --ink-outline: #3f8f8a;
    --white: #fbf6ea;
  }
  * { margin: 0; padding: 0; box-sizing: border-box; }
  html, body { width: 849px; height: 1200px; overflow: hidden; }
  body { font-family: "Josefin Sans", "Arial Narrow", sans-serif; font-weight: 600; }
  .flyer {
    position: relative;
    width: 849px;
    height: 1200px;
    overflow: hidden;
    background: radial-gradient(ellipse at 55% 45%, var(--paper-light) 0%, var(--paper-mid) 65%, var(--paper-edge) 100%);
  }
  .stripe-area { position: absolute; inset: 0; }
  .shop-name {
    position: absolute;
    left: 70px;
    top: 82px;
    font-size: 34px;
    color: var(--ink);
    letter-spacing: 1px;
    white-space: nowrap;
  }
  .headline {
    position: absolute;
    left: 330px;
    top: 160px;
    width: 500px;
    text-align: center;
    font-family: "Rochester", cursive;
    font-weight: 400;
    color: var(--ink);
    -webkit-text-stroke: 0.6px var(--ink-outline);
    line-height: 1;
    white-space: nowrap;
  }
  .headline .line-one { display: block; font-size: 58px; }
  .headline .line-one sup { font-size: 30px; vertical-align: 24px; }
  .headline .line-two { display: block; font-size: 70px; margin-top: 20px; }
  .band-text {
    position: absolute;
    color: var(--white);
    font-size: 21px;
    letter-spacing: 2px;
    text-transform: uppercase;
    white-space: nowrap;
    transform-origin: left center;
  }
  .band-text sup { font-size: 12px; vertical-align: 7px; }
  .invite { left: 55px; top: 348px; transform: rotate(28deg); }
  .celebrate { left: 447px; top: 478px; }
  .date-label { left: 258px; top: 572px; transform: rotate(-15deg); }
  .date-value { left: 412px; top: 543px; }
  .time { left: 574px; top: 618px; }
  .time small { font-size: 15px; }
  .address { left: 42px; top: 905px; transform: rotate(-48deg); }
  .contact { left: 66px; top: 1170px; transform: rotate(-55deg); }
  .contact .gap { display: inline-block; width: 36px; }
  .festivities {
    position: absolute;
    left: 430px;
    top: 740px;
    list-style: none;
    color: var(--ink);
    font-size: 25px;
    letter-spacing: 2px;
    text-transform: uppercase;
    line-height: 1;
    white-space: nowrap;
  }
  .festivities li { margin-bottom: 24px; }
  .festivities li.two-line { line-height: 0.95; }
</style>
</head>
<body>
<main class="flyer">
  <svg class="stripe-area" width="849" height="1200" viewBox="0 0 849 1200" role="img" aria-label="Retro converging stripe bands in green, teal, mustard, orange and red">
    <defs>
      <linearGradient id="stripe-tones" x1="0" y1="0" x2="0.3" y2="1">
        <stop offset="0" stop-color="var(--tone-green)"/>
        <stop offset="0.25" stop-color="var(--tone-teal)"/>
        <stop offset="0.5" stop-color="var(--tone-mustard)"/>
        <stop offset="0.75" stop-color="var(--tone-orange)"/>
        <stop offset="1" stop-color="var(--tone-red)"/>
      </linearGradient>
    </defs>
    <path fill="url(#stripe-tones)" d="M0 240 L380 440 Q410 455 460 456 L849 456 L849 700 L470 702 Q435 706 410 745 L195 1200 L0 1200 Z"/>
  </svg>

  <p class="shop-name">1920 Vintage</p>

  <h1 class="headline">
    <span class="line-one">Happy 1<sup>st</sup> Birthday</span>
    <span class="line-two">1920 Vintage!</span>
  </h1>

  <p class="band-text invite">You are invited to help</p>
  <p class="band-text celebrate">Celebrate in the festivities!</p>
  <p class="band-text date-label">Date:</p>
  <p class="band-text date-value">19<sup>th</sup> &amp; 20<sup>th</sup> July</p>
  <p class="band-text time">From 11:00<small>AM</small></p>
  <p class="band-text address">1920 Harbour Bay Rd, Elmwood</p>
  <p class="band-text contact">Ph: 55 210...<span class="gap"></span>Mobile: 0400123456</p>

  <ul class="festivities">
    <li>Festivities will include:</li>
    <li>Pop up market stalls,</li>
    <li class="two-line">Best dressed<br>vintage outfit,</li>
    <li>Face painting</li>
    <li>Vintage cars on display</li>
    <li>Music</li>
    <li>Refreshments</li>
    <li>50s hairstyles</li>
  </ul>
</main>
</body>
</html>
```